Creative, Colorful, Dynamic Infographic for Global Non-Profit

We are a global arts and education non-profit in need of an infographic that illustrates four key skills embedded in our work: Curiosity, Listening, Imagination, Postive Action.
We work primarily with educators, students, and artists who use the power of personal stories to build community and connection and to bridge divides.
Our new brand guidelines, logos, and fonts are here: https://stylekit.example/lanternfold-9
I've attached a mock-up of the graphic and the required text. (Note the attached design was created by a staff person, your final design does not need to be the same. The color scheme and text of the final design should match the brand guidelines above.)
The graphic will be used for both web and print media and should include the purple Lanternfold 9 logo (also attached).
Ideally the final design will delight audiences and spark interest in our work.

```html
<!DOCTYPE html>
<html lang="en">
<head>
<meta charset="utf-8">
<title>Lanternfold 9 – Four Skills</title>
<link rel="stylesheet" href="https://fonts.googleapis.com/css2?family=Bodoni+Moda:wght@500;600&family=Work+Sans:wght@500;600&display=swap">
<style>
  :root {
    --paper: #f5e9d8;
    --white: #ffffff;
    --navy: #1c1c38;
    --blue: #2c6bb3;
    --red: #ee4342;
    --yellow: #e7c946;
    --purple: #673694;
  }
  html, body { margin: 0; padding: 0; overflow: hidden; }
  body { width: 848px; height: 1200px; background: var(--paper); }
  .skills-wheel { display: block; width: 848px; height: 1200px; }
  .skill-title { font-family: "Bodoni Moda", "Times New Roman", serif; font-weight: 600; font-size: 34px; fill: var(--white); }
  .skill-copy { font-family: "Work Sans", Arial, sans-serif; font-weight: 500; font-size: 15px; fill: var(--white); }
  .ring-copy { font-family: "Work Sans", Arial, sans-serif; font-weight: 500; font-size: 13.5px; }
  .brand-name { font-family: "Work Sans", Arial, sans-serif; font-weight: 600; font-size: 15px; fill: var(--white); }
  .flow { fill: none; stroke-width: 2; }
  .flow--dashed { stroke-dasharray: 4 4; stroke-width: 1.5; }
</style>
</head>
<body>
<svg class="skills-wheel" viewBox="0 0 1060 1500" xmlns="http://www.w3.org/2000/svg" role="img" aria-label="Four skills cycle: Positive Action, Curiosity, Listening, Imagination">
  <defs>
    <radialGradient id="floor-shadow">
      <stop offset="0" stop-color="#bfae98" stop-opacity="0.75"/>
      <stop offset="1" stop-color="#bfae98" stop-opacity="0"/>
    </radialGradient>
    <marker id="head-navy" markerWidth="10" markerHeight="10" refX="7" refY="5" orient="auto" markerUnits="userSpaceOnUse"><path d="M0,0 L10,5 L0,10 L3,5 Z" fill="var(--navy)"/></marker>
    <marker id="head-blue" markerWidth="10" markerHeight="10" refX="7" refY="5" orient="auto" markerUnits="userSpaceOnUse"><path d="M0,0 L10,5 L0,10 L3,5 Z" fill="var(--blue)"/></marker>
    <marker id="head-red" markerWidth="10" markerHeight="10" refX="7" refY="5" orient="auto" markerUnits="userSpaceOnUse"><path d="M0,0 L10,5 L0,10 L3,5 Z" fill="var(--red)"/></marker>
    <marker id="head-yellow" markerWidth="10" markerHeight="10" refX="7" refY="5" orient="auto" markerUnits="userSpaceOnUse"><path d="M0,0 L10,5 L0,10 L3,5 Z" fill="var(--yellow)"/></marker>

    <path id="ring-action" d="M190,670 A345,345 0 0 1 542,385"/>
    <path id="ring-curiosity" d="M659,410 A345,345 0 0 1 854,612"/>
    <path id="ring-listening" d="M590,1073 A348,348 0 0 0 870,802"/>
    <path id="ring-imagination" d="M194,820 A348,348 0 0 0 422,1061"/>
  </defs>

  <ellipse class="floor-shadow" cx="530" cy="1245" rx="270" ry="32" fill="url(#floor-shadow)"/>

  <!-- flow arrows -->
  <g class="flows">
    <path class="flow" stroke="var(--navy)" marker-end="url(#head-navy)" d="M168,598 A385,385 0 0 1 512,345"/>
    <path class="flow flow--dashed" stroke="var(--navy)" marker-end="url(#head-navy)" d="M130,730 A400,400 0 0 1 400,352"/>
    <path class="flow" stroke="var(--blue)" marker-end="url(#head-blue)" d="M662,368 A385,385 0 0 1 911,720"/>
    <path class="flow flow--dashed" stroke="var(--blue)" marker-end="url(#head-blue)" d="M530,330 A400,400 0 0 1 906,600"/>
    <path class="flow" stroke="var(--red)" marker-end="url(#head-red)" d="M892,862 A385,385 0 0 1 552,1114"/>
    <path class="flow flow--dashed" stroke="var(--red)" marker-end="url(#head-red)" d="M930,730 A400,400 0 0 1 664,1106"/>
    <path class="flow" stroke="var(--yellow)" marker-end="url(#head-yellow)" d="M420,1098 A385,385 0 0 1 152,732"/>
    <path class="flow flow--dashed" stroke="var(--yellow)" marker-end="url(#head-yellow)" d="M530,1130 A400,400 0 0 1 154,845"/>
  </g>

  <circle class="wheel-base" cx="530" cy="730" r="362" fill="var(--white)"/>

  <!-- quadrants -->
  <path class="quadrant quadrant--action" d="M517,717 L217,717 A300,300 0 0 1 517,417 Z" fill="var(--navy)" stroke="var(--navy)" stroke-width="20" stroke-linejoin="round"/>
  <path class="quadrant quadrant--curiosity" d="M545,717 L545,417 A300,300 0 0 1 845,717 Z" fill="var(--blue)" stroke="var(--blue)" stroke-width="20" stroke-linejoin="round"/>
  <path class="quadrant quadrant--listening" d="M545,745 L845,745 A300,300 0 0 1 545,1045 Z" fill="var(--red)" stroke="var(--red)" stroke-width="20" stroke-linejoin="round"/>
  <path class="quadrant quadrant--imagination" d="M517,745 L517,1045 A300,300 0 0 1 217,745 Z" fill="var(--yellow)" stroke="var(--yellow)" stroke-width="20" stroke-linejoin="round"/>

  <!-- ring captions -->
  <text class="ring-copy" fill="var(--navy)"><textPath href="#ring-action" startOffset="4">Your positive actions will make you curious about what else is possible</textPath></text>
  <text class="ring-copy" fill="var(--blue)"><textPath href="#ring-curiosity" startOffset="8">Your curiosity will allow you to listen</textPath></text>
  <text class="ring-copy" fill="var(--red)"><textPath href="#ring-listening" startOffset="8">Your listening will allow you to take in new information</textPath></text>
  <text class="ring-copy" fill="var(--yellow)"><textPath href="#ring-imagination" startOffset="4">Your imagination identifies positive actions</textPath></text>

  <!-- icons -->
  <g class="icon icon--thumb" fill="var(--white)">
    <rect x="437" y="478" width="9" height="30" rx="2"/>
    <path d="M450,478 L458,466 C460,462 466,463 466,468 L464,477 L478,477 C482,477 484,481 482,485 L478,505 C477,508 475,509 472,509 L450,509 Z"/>
  </g>
  <g class="icon icon--eye" fill="none" stroke="var(--white)" stroke-width="3.5" stroke-linecap="round">
    <path d="M574,486 Q595,466 616,486 Q595,506 574,486 Z"/>
    <circle cx="595" cy="486" r="5" fill="var(--white)" stroke="none"/>
    <path d="M574,465 L579,470 M616,465 L611,470 M574,507 L579,502 M616,507 L611,502"/>
  </g>
  <g class="icon icon--chat" fill="var(--white)">
    <path d="M462,812 C474,812 482,820 482,829 C482,838 474,845 463,845 L450,849 L453,841 C447,838 443,834 443,829 C443,820 451,812 462,812 Z"/>
    <path d="M486,826 L486,852 L476,846 C470,846 465,844 462,842 C475,840 484,834 486,826 Z"/>
  </g>
  <g class="icon icon--speaker" fill="var(--white)">
    <path d="M574,830 L586,830 L603,820 L603,855 L586,845 L574,845 Z"/>
    <rect x="610" y="828" width="4" height="19" rx="2"/>
    <rect x="619" y="824" width="4" height="27" rx="2"/>
  </g>

  <!-- skill text -->
  <g class="skill skill--action" text-anchor="end">
    <text class="skill-title" x="488" y="560">Positive</text>
    <text class="skill-title" x="488" y="593">Action</text>
    <text class="skill-copy" x="488" y="625">Show that your words</text>
    <text class="skill-copy" x="488" y="644">and actions matter</text>
  </g>
  <g class="skill skill--curiosity">
    <text class="skill-title" x="569" y="563">Curiosity</text>
    <text class="skill-copy" x="571" y="594">Focus on how you can learn</text>
    <text class="skill-copy" x="571" y="613">from another’s knowledge</text>
    <text class="skill-copy" x="571" y="632">and experience  your</text>
    <text class="skill-copy" x="571" y="651">curiosity allows you to listen</text>
  </g>
  <g class="skill skill--imagination" text-anchor="end">
    <text class="skill-title" x="488" y="898">Imagination</text>
    <text class="skill-copy" x="488" y="924">Consider possibilities</text>
    <text class="skill-copy" x="488" y="943">beyond what</text>
    <text class="skill-copy" x="488" y="962">you already know</text>
  </g>
  <g class="skill skill--listening">
    <text class="skill-title" x="573" y="902">Listening</text>
    <text class="skill-copy" x="575" y="933">Work to understand</text>
    <text class="skill-copy" x="575" y="952">before using words.</text>
  </g>

  <!-- brand hub -->
  <circle class="brand-hub" cx="530" cy="730" r="64" fill="var(--purple)" stroke="var(--white)" stroke-width="6"/>
  <text class="brand-name" x="530" y="735" text-anchor="middle">Lanternfold 9</text>
</svg>
</body>
</html>
```